I want both print and ebook covers

book title is "The Classroom MEETING HANDBOOK: Fresh Paths to Partner With Families For Pupil Growth. I want a dark Teal or Navy Background. Yellow and white letters. Distorted Picture of one teacher, two parents and one child around a table or desk. But no Martians! My name should include "Award Winning Author"

Target Market(s)

teachers and other educators--principals, school psychologists, speech therapists, etc.

Industry/Entity Type

schools

• I just need to see how it looks

Colors
0054AA
0677BA
7BADD7
CADEEF
E8F1F8
0094D4
00A9DD
6FCCEA
C7EBF8
E9F6FB
FFC000
F8CF3A
FAE287
FDF2CF
FEFAEE

Requirements
Must have
• Title top third of page big enough to be read when reduced greatly in size. Contrast so that it "pops'.
Nice to have
• Teacher, two parents and one child around a table/desk. My name should include 'Award winning author'

```html
<!DOCTYPE html>
<html lang="en">
<head>
<meta charset="utf-8">
<title>The Classroom Meeting Handbook – Cover</title>
<link rel="stylesheet" href="https://fonts.googleapis.com/css2?family=Jost:ital,wght@0,500;0,600;1,300&family=Oswald:wght@500&display=swap">
<style>
  :root {
    --page-bg: #ffffff;
    --navy-deep: #04053f;
    --navy-mid: #0c1190;
    --navy-glow: #1b26c4;
    --title-white: #ffffff;
    --title-yellow: #ffe600;
    --scene-light: #7badd7;
    --scene-mid: #3f5fc4;
    --scene-dark: #0c1a7a;
  }
  * { box-sizing: border-box; margin: 0; padding: 0; }
  html, body {
    width: 1200px;
    height: 675px;
    overflow: hidden;
    background: var(--page-bg);
  }
  .stage {
    width: 1200px;
    height: 675px;
    display: flex;
    align-items: center;
    justify-content: center;
  }
  .cover {
    width: 414px;
    height: 640px;
    background: radial-gradient(ellipse 75% 60% at 50% 55%, var(--navy-glow) 0%, var(--navy-mid) 45%, var(--navy-deep) 100%);
    display: flex;
    flex-direction: column;
    align-items: center;
    padding: 34px 46px 30px;
    color: var(--title-white);
    font-family: "Jost", "Futura", sans-serif;
  }
  .title { width: 100%; text-align: center; }
  .ruled {
    display: flex;
    align-items: center;
    gap: 8px;
    width: 100%;
  }
  .ruled::before, .ruled::after {
    content: "";
    flex: 1;
    height: 3px;
    background: var(--title-white);
  }
  .title-the {
    font-weight: 600;
    font-size: 27px;
    line-height: 1;
  }
  .title-main {
    font-weight: 600;
    font-size: 54px;
    line-height: 1.02;
    letter-spacing: -1px;
    white-space: nowrap;
    margin-top: 4px;
  }
  .title-accent {
    color: var(--title-yellow);
    font-weight: 600;
    font-size: 74px;
    line-height: 1;
    letter-spacing: -1px;
    white-space: nowrap;
  }
  .title-end {
    font-weight: 300;
    font-style: italic;
    font-size: 40px;
    line-height: 1.1;
    letter-spacing: 1px;
    margin-top: 2px;
  }
  .title-end::before, .title-end::after { height: 3px; }
  .subtitle {
    font-family: "Oswald", "Arial Narrow", sans-serif;
    font-weight: 500;
    font-size: 17px;
    letter-spacing: -0.2px;
    margin-top: 28px;
    white-space: nowrap;
  }
  .scene {
    width: 290px;
    height: 168px;
    margin-top: 26px;
    border-radius: 6px;
    background: radial-gradient(ellipse at 50% 60%, var(--scene-light) 0%, var(--scene-mid) 55%, var(--scene-dark) 100%);
  }
  .credit {
    margin-top: auto;
    text-align: center;
  }
  .award {
    color: var(--title-yellow);
    font-weight: 600;
    font-size: 11px;
    letter-spacing: 0.3px;
  }
  .author {
    font-weight: 500;
    font-size: 33px;
    letter-spacing: 0.5px;
    margin-top: 8px;
  }
</style>
</head>
<body>
  <main class="stage">
    <article class="cover">
      <h1 class="title">
        <span class="ruled title-the">THE</span>
        <span class="title-main" style="display:block">CLASSROOM</span>
        <span class="title-accent" style="display:block">MEETING</span>
        <span class="ruled title-end">HANDBOOK</span>
      </h1>
      <p class="subtitle">Fresh Paths to Partner With Families For Pupil Growth</p>
      <div class="scene" role="img" aria-label="Flat illustration of a teacher, two parents and a child meeting around a desk with a potted plant"></div>
      <footer class="credit">
        <p class="award">AWARD WINNING AUTHOR</p>
        <p class="author">AUTHOR NAME</p>
      </footer>
    </article>
  </main>
</body>
</html>
```